Generator Control - Superyacht Power Management System

We need a graphic design for a Touch Screen interface to control generators on Superyachts. We have a layout of the control system worked out, but need nice graphics to go with it.
The graphics comes down to a 300x460px App that i replicate several times on my 15" touchscreen as required.
See attached images.
The interface is divided up into 4 sections:
• Section#1 - 4 rectangles for the control
• Section#2 - a vertical bar graph,
• Section#3 - a section to display custom information
• Section#4 - a circuit breaker symbol.
The dimensions in pixels must be as per the attached image.
SECTION#1:
The 4 control rectangles correspond to 4 control modes:
• STOP – colours based on RED
• RUN – colours based on ORANGE
• RUN ONLINE – colours based on GREEN
• AUTO – colours based on BLUE
• THE TEXT DOESN’T HAVE TO BE ON THE GRAPHICS, WE JUST NEED THE BACKGROUND FOR THE TEXT, I ADD THE TEXT LATER USING SOFTWARE.
Each control rectangle needs to have 3 clearly identifiable states:
• Active/Selected (this is the currently active mode)
• Not Active/Not Selected (this mode is available but not currently active)
• Unavailable (this mode is not available)
SECTION#2:
The vertical bar graph design only needs the outline/frame of the bar graph. The actual moving part can be left blank; I will add that in later using an animation.
SECTION#3:
Free to look good as you want. See attached image for reference.
Within section#3 (at the top) is a 40x240px subsection, and should simply by 2 states, green or 'background colour of section#3 '. (green for when the generator is running, blend with the rest of section#3 when it is not). There are about 10 different texts I add on top of that square using software, corresponding to the status of the generator (starting, deloading, synchronizing, etc.)
SECTION#4:
Graphical representation of an electrical switch. Can be in two positions: opened or closed. See attached image as reference.

Target Market(s)

Cheif Engineers /Captains on Superyachts

Industry/Entity Type

Graphic Design

Requirements
Must have
• Must have the same graphics style as the uploaded file#2

```html
<!DOCTYPE html>
<html lang="en">
<head>
<meta charset="utf-8">
<title>Generator Control Panel</title>
<link href="https://fonts.googleapis.com/css2?family=Signika:wght@500;600&family=Open+Sans:wght@400;600;700&display=swap" rel="stylesheet">
<style>
  :root {
    --page: #ffffff;
    --green-top: #74c55a;
    --green-bottom: #3e9a3a;
    --green-edge: #5aae49;
    --orange-top: #ffb02a;
    --orange-bottom: #ff7300;
    --orange-edge: #f39212;
    --red-top: #f58c8c;
    --red-bottom: #e04747;
    --red-edge: #e86a6a;
    --blue-top: #5db3ea;
    --blue-bottom: #1d77c6;
    --blue-edge: #3b93d6;
    --grey-top: #bdbdbd;
    --grey-bottom: #8c8c8c;
    --grey-edge: #9e9e9e;
    --active-ring: #ffffff;
    --panel-dark: #1b1b1b;
    --panel-dark-2: #242424;
    --grid-line: #8a8a8a;
    --text-light: #ffffff;
    --text-dark: #1e1e1e;
    --header-top: #f6f6f6;
    --header-bottom: #d9d9d9;
    --running-top: #6cc04f;
    --running-bottom: #3f963a;
    --seg-red: #8a1010;
    --seg-red-hi: #a81a1a;
    --seg-orange: #a9620c;
    --seg-orange-hi: #c27414;
    --seg-green: #3c6629;
    --seg-green-hi: #4b7a34;
  }
  * { box-sizing: border-box; margin: 0; padding: 0; }
  html, body {
    width: 1200px; height: 1100px; overflow: hidden;
    background: var(--page);
  }
  .stage { position: relative; width: 1200px; height: 1100px; }

  /* Control buttons: base look = available, not selected */
  .control {
    position: absolute; width: 340px; height: 220px;
    border-radius: 12px;
    display: flex; flex-direction: column; align-items: center; justify-content: center; gap: 16px;
    font-family: "Signika", sans-serif; font-weight: 600; font-size: 54px; line-height: 1;
    color: var(--text-light);
    text-shadow: 0 2px 3px rgba(0,0,0,0.25);
    box-shadow: inset 0 2px 0 rgba(255,255,255,0.35);
  }
  .control svg { width: 48px; height: 48px; filter: drop-shadow(0 2px 2px rgba(0,0,0,0.2)); }
  .control--online { left: 146px; top: 24px; background: linear-gradient(var(--green-top), var(--green-bottom)); border: 3px solid var(--green-edge); }
  .control--run    { left: 500px; top: 24px; background: linear-gradient(var(--orange-top), var(--orange-bottom)); border: 3px solid var(--orange-edge); }
  .control--stop   { left: 146px; top: 260px; background: linear-gradient(var(--red-top), var(--red-bottom)); border: 3px solid var(--red-edge); }
  .control--auto   { left: 500px; top: 260px; background: linear-gradient(var(--blue-top), var(--blue-bottom)); border: 3px solid var(--blue-edge); }
  .control__count { font-size: 50px; letter-spacing: 10px; padding-left: 10px; }

  /* Control states */
  .control.is-active {
    border-color: var(--active-ring);
    box-shadow: inset 0 2px 0 rgba(255,255,255,0.45), 0 0 0 3px rgba(0,0,0,0.35), 0 0 18px rgba(255,255,255,0.6);
  }
  .control.is-unavailable {
    background: linear-gradient(var(--grey-top), var(--grey-bottom));
    border-color: var(--grey-edge);
    color: rgba(255,255,255,0.6);
    text-shadow: none;
    box-shadow: none;
  }

  /* Load bar graph */
  .load-meter {
    position: absolute; left: 852px; top: 24px; width: 164px; height: 1056px;
    background: repeating-linear-gradient(45deg, var(--panel-dark) 0 3px, var(--panel-dark-2) 3px 6px);
    border: 2px solid #3a3a3a;
    font-family: "Open Sans", sans-serif; color: var(--text-light); font-weight: 700;
  }
  .load-meter__percent { position: absolute; top: 20px; width: 100%; text-align: center; font-size: 40px; }
  .load-meter__power { position: absolute; bottom: 14px; width: 100%; text-align: center; font-size: 40px; }
  .load-meter__power small { font-size: 28px; }
  .load-meter__scale { position: absolute; left: 20px; top: 92px; width: 120px; height: 880px; }

  /* Status strip: grey when stopped, green when running */
  .status {
    position: absolute; left: 152px; top: 500px; width: 680px; height: 96px;
    background: linear-gradient(var(--header-top), var(--header-bottom));
    border: 2px solid #c4c4c4;
    font-family: "Open Sans", sans-serif; font-weight: 700; font-size: 40px; color: var(--text-dark);
    display: flex; align-items: center; padding-left: 38px;
  }
  .status.is-running {
    background: linear-gradient(var(--running-top), var(--running-bottom));
    border-color: var(--green-edge);
    color: var(--text-light);
  }

  /* Data table */
  .readings {
    position: absolute; left: 152px; top: 600px; width: 680px; height: 480px;
    background: repeating-linear-gradient(45deg, var(--panel-dark) 0 3px, var(--panel-dark-2) 3px 6px);
    font-family: "Open Sans", sans-serif; color: var(--text-light);
    display: grid; grid-template-columns: 404px 276px;
  }
  .engine-list { border-right: 2px solid var(--grid-line); display: grid; grid-template-rows: repeat(4, 120px); }
  .engine-item { display: grid; grid-template-columns: 96px 1fr; border-bottom: 2px solid var(--grid-line); }
  .engine-item:last-child { border-bottom: none; }
  .engine-item__icon { border-right: 2px solid var(--grid-line); display: flex; align-items: center; justify-content: center; }
  .engine-item__icon svg { width: 56px; height: 56px; }
  .engine-item__body { padding: 14px 0 0 16px; }
  .engine-item__label { font-weight: 700; font-size: 36px; line-height: 44px; }
  .engine-item__value { font-size: 32px; line-height: 42px; word-spacing: 4px; }

  .electrical { display: grid; grid-template-rows: 180px 180px 120px; }
  .electrical__group { border-bottom: 2px solid var(--grid-line); padding-top: 6px; }
  .electrical__group:last-child { border-bottom: none; }
  .reading { display: grid; grid-template-columns: 156px 1fr; column-gap: 14px; font-size: 34px; line-height: 56px; }
  .reading__num { text-align: right; }
</style>
</head>
<body>
<div class="stage">

  <div class="control control--online is-available">
    <span>Run Online</span>
    <svg viewBox="0 0 52 52" aria-hidden="true">
      <circle cx="26" cy="26" r="12" fill="none" stroke="#fff" stroke-width="3"/>
      <path d="M20 20 q4 2 3 6 q-2 2 0 5 M30 17 q-2 4 2 6 q3 1 4 4" fill="none" stroke="#fff" stroke-width="2.5"/>
      <path d="M10 20 A17 17 0 0 1 38 10" fill="none" stroke="#fff" stroke-width="3.5"/>
      <path d="M36 4 L42 12 L33 14 Z" fill="#fff"/>
      <path d="M42 32 A17 17 0 0 1 14 42" fill="none" stroke="#fff" stroke-width="3.5"/>
      <path d="M16 48 L10 40 L19 38 Z" fill="#fff"/>
    </svg>
  </div>

  <div class="control control--run is-available">
    <span>Run</span>
    <svg viewBox="0 0 52 52" aria-hidden="true">
      <g fill="#fff" transform="translate(26 26)">
        <rect x="-5" y="-23" width="10" height="12" rx="2"/>
        <rect x="-5" y="-23" width="10" height="12" rx="2" transform="rotate(45)"/>
        <rect x="-5" y="-23" width="10" height="12" rx="2" transform="rotate(90)"/>
        <rect x="-5" y="-23" width="10" height="12" rx="2" transform="rotate(135)"/>
        <rect x="-5" y="-23" width="10" height="12" rx="2" transform="rotate(180)"/>
        <rect x="-5" y="-23" width="10" height="12" rx="2" transform="rotate(225)"/>
        <rect x="-5" y="-23" width="10" height="12" rx="2" transform="rotate(270)"/>
        <rect x="-5" y="-23" width="10" height="12" rx="2" transform="rotate(315)"/>
        <circle r="15"/>
      </g>
      <circle cx="26" cy="26" r="6" fill="#ff8c10"/>
    </svg>
  </div>

  <div class="control control--stop is-available">
    <span>Stop</span>
    <svg viewBox="0 0 52 52" aria-hidden="true">
      <circle cx="26" cy="26" r="22" fill="#fff"/>
      <path d="M18 18 L34 34 M34 18 L18 34" stroke="#e45656" stroke-width="6" stroke-linecap="round"/>
    </svg>
  </div>

  <div class="control control--auto is-available">
    <span>Automatic</span>
    <span class="control__count">(1)</span>
  </div>

  <div class="load-meter">
    <div class="load-meter__percent">0%</div>
    <svg class="load-meter__scale" viewBox="0 0 120 880" aria-label="Generator load scale">
      <g>
        <rect x="0" y="0"   width="120" height="36" rx="5" fill="var(--seg-red-hi)"/>
        <rect x="0" y="44"  width="120" height="36" rx="5" fill="var(--seg-red)"/>
        <rect x="0" y="88"  width="120" height="36" rx="5" fill="var(--seg-red)"/>
        <rect x="0" y="132" width="120" height="36" rx="5" fill="var(--seg-orange-hi)"/>
        <rect x="0" y="176" width="120" height="36" rx="5" fill="var(--seg-orange)"/>
        <rect x="0" y="220" width="120" height="36" rx="5" fill="var(--seg-orange)"/>
        <rect x="0" y="264" width="120" height="36" rx="5" fill="var(--seg-green-hi)"/>
        <rect x="0" y="308" width="120" height="36" rx="5" fill="var(--seg-green)"/>
        <rect x="0" y="352" width="120" height="36" rx="5" fill="var(--seg-green)"/>
        <rect x="0" y="396" width="120" height="36" rx="5" fill="var(--seg-green)"/>
        <rect x="0" y="440" width="120" height="36" rx="5" fill="var(--seg-green)"/>
        <rect x="0" y="484" width="120" height="36" rx="5" fill="var(--seg-green)"/>
        <rect x="0" y="528" width="120" height="36" rx="5" fill="var(--seg-green)"/>
        <rect x="0" y="572" width="120" height="36" rx="5" fill="var(--seg-green)"/>
        <rect x="0" y="616" width="120" height="36" rx="5" fill="var(--seg-green)"/>
        <rect x="0" y="660" width="120" height="36" rx="5" fill="var(--seg-green)"/>
        <rect x="0" y="704" width="120" height="36" rx="5" fill="var(--seg-green)"/>
        <rect x="0" y="748" width="120" height="36" rx="5" fill="var(--seg-green)"/>
        <rect x="0" y="792" width="120" height="36" rx="5" fill="var(--seg-green)"/>
        <rect x="0" y="836" width="120" height="36" rx="5" fill="var(--seg-green)"/>
      </g>
    </svg>
    <div class="load-meter__power">0<small>KW</small></div>
  </div>

  <div class="status">Running - Offline</div>

  <div class="readings">
    <div class="engine-list">
      <div class="engine-item">
        <div class="engine-item__icon">
          <svg viewBox="0 0 56 56" aria-hidden="true">
            <rect x="22" y="6" width="10" height="32" rx="5" fill="#d8dde6"/>
            <circle cx="27" cy="42" r="9" fill="#4a9be0"/>
            <rect x="25" y="22" width="4" height="20" fill="#4a9be0"/>
            <path d="M10 30 q-4 6 0 9 q4 -3 0 -9 Z" fill="#6fb6f0"/>
          </svg>
        </div>
        <div class="engine-item__body">
          <div class="engine-item__label">Water Temp</div>
          <div class="engine-item__value">83 °C</div>
        </div>
      </div>
      <div class="engine-item">
        <div class="engine-item__icon">
          <svg viewBox="0 0 56 56" aria-hidden="true">
            <circle cx="28" cy="30" r="18" fill="#d9d9d9" stroke="#9a9a9a" stroke-width="3"/>
            <circle cx="28" cy="30" r="12" fill="#f2f2f2"/>
            <path d="M28 30 L20 22" stroke="#333" stroke-width="3" stroke-linecap="round"/>
            <rect x="24" y="6" width="8" height="7" fill="#9a9a9a"/>
          </svg>
        </div>
        <div class="engine-item__body">
          <div class="engine-item__label">Oil Pressure</div>
          <div class="engine-item__value">3.8 BAR</div>
        </div>
      </div>
      <div class="engine-item">
        <div class="engine-item__icon">
          <svg viewBox="0 0 56 56" aria-hidden="true">
            <circle cx="28" cy="28" r="22" fill="#3a3a3a" stroke="#7a7a7a" stroke-width="3"/>
            <path d="M12 34 A17 17 0 0 1 22 13" fill="none" stroke="#4caf50" stroke-width="5"/>
            <path d="M22 13 A17 17 0 0 1 38 14" fill="none" stroke="#f0a020" stroke-width="5"/>
            <path d="M38 14 A17 17 0 0 1 44 34" fill="none" stroke="#e03c3c" stroke-width="5"/>
            <path d="M28 30 L18 22" stroke="#fff" stroke-width="3" stroke-linecap="round"/>
          </svg>
        </div>
        <div class="engine-item__body">
          <div class="engine-item__label">RPM</div>
          <div class="engine-item__value">1500</div>
        </div>
      </div>
      <div class="engine-item">
        <div class="engine-item__icon">
          <svg viewBox="0 0 56 56" aria-hidden="true">
            <circle cx="28" cy="28" r="19" fill="none" stroke="#8a8a8a" stroke-width="4"/>
            <path d="M28 16 V28 L36 33" fill="none" stroke="#8a8a8a" stroke-width="3.5" stroke-linecap="round"/>
          </svg>
        </div>
        <div class="engine-item__body">
          <div class="engine-item__label">Online Time</div>
          <div class="engine-item__value">0h &nbsp; 0m &nbsp; 0s</div>
        </div>
      </div>
    </div>

    <div class="electrical">
      <div class="electrical__group">
        <div class="reading"><span class="reading__num">230</span><span>VAC</span></div>
        <div class="reading"><span class="reading__num">400</span><span>VAC</span></div>
        <div class="reading"><span class="reading__num">50.0</span><span>HZ</span></div>
      </div>
      <div class="electrical__group">
        <div class="reading"><span class="reading__num">0</span><span>A L1</span></div>
        <div class="reading"><span class="reading__num">0</span><span>A L2</span></div>
        <div class="reading"><span class="reading__num">0</span><span>A L3</span></div>
      </div>
      <div class="electrical__group">
        <div class="reading"><span class="reading__num">0</span><span>KVA</span></div>
        <div class="reading"><span class="reading__num">0.00</span><span>PF</span></div>
      </div>
    </div>
  </div>

</div>
</body>
</html>
```